Copper Ridge Stewardship Summit needs a marketing flyer

We need a full page graphic for our upcoming Forum that can also be converted into a website "header" for social media, etc.: "Copper Ridge Stewardship Summit - Making Impact Through the Built Environment"

INTRODUCTION:
During the first week of August 2022, Q-VarDT is presenting the Copper Ridge Stewardship Summit - Making Impact Through the Built Environment.

One of the most exciting aspects of this conference will be the bringing together of multiple organizations including for-profits and nonprofits, K-12’s and higher education, cities and counties and other governmental agencies, as well as architects, engineers, and contractors to collaboratively present and discuss issues and ideas related to sustainability, with a Texas focus.

This event will be a catalyst for public and private project owners to holistically gather information and momentum as we bring the resources and vision needed to achieve the goal of zero carbon emissions from the built environment by 2040, and address water, green space and the natural environment, transportation, equity, and funding, among other topics.

```html
<!DOCTYPE html>
<html lang="en">
<head>
<meta charset="utf-8">
<title>Copper Ridge Stewardship Summit – Flyer</title>
<link rel="stylesheet" href="https://fonts.googleapis.com/css2?family=Montserrat:wght@400;500;600;700;800&family=Oswald:wght@600&display=swap">
<style>
  :root{
    --blue:#1f3d99;
    --blue-deep:#18338a;
    --green:#8cb43c;
    --grey-text:#444;
    --dark:#3b3b3b;
    --paper:#ffffff;
    --stage:#eeeeee;
    --swoosh:#e6e6e0;
  }
  *{margin:0;padding:0;box-sizing:border-box}
  html,body{width:1200px;height:2416px;overflow:hidden;background:var(--stage)}
  body{font-family:"Montserrat",Arial,sans-serif;color:var(--blue)}
  .flyer{position:absolute;left:50px;top:496px;width:1100px;height:1424px;background:var(--paper);overflow:hidden;box-shadow:0 6px 18px rgba(0,0,0,.25)}
  .deco{position:absolute;left:0;top:0}
  .brand{position:absolute;left:71px;top:46px;height:112px;display:flex;align-items:center;gap:28px}
  .brand-dot{width:112px;height:112px;border-radius:50%;background:var(--blue);flex:none}
  .brand-name{font-size:54px;line-height:1;font-weight:600;color:var(--blue);letter-spacing:1px}
  .title{position:absolute;left:46px;top:224px;font-family:"Oswald",Arial,sans-serif;font-weight:600;font-size:74px;line-height:73px;color:var(--blue);text-transform:uppercase}
  .subtitle{position:absolute;left:46px;top:462px;width:480px;font-size:34px;line-height:43px;font-weight:700;color:var(--green)}
  .rule{position:absolute;left:46px;top:556px;width:466px;height:4px;background:var(--blue)}
  .presenting{position:absolute;left:46px;top:582px;font-size:34px;line-height:43px;font-weight:700;color:var(--blue);text-transform:uppercase;letter-spacing:.5px}
  .tagline{position:absolute;left:46px;top:716px;font-size:27px;font-weight:500;color:var(--grey-text)}
  .week-band{position:absolute;left:46px;top:808px;font-size:30px;font-weight:700;color:#fff;text-transform:uppercase}
  .date{position:absolute;left:604px;top:792px;font-size:64px;font-weight:800;color:var(--dark);letter-spacing:-1px}
  .groups-intro{position:absolute;left:50px;top:890px;font-size:17px;line-height:21px;font-weight:700;color:var(--blue);text-transform:uppercase}
  .groups-intro em{font-style:normal;color:var(--green)}
  .groups{position:absolute;left:50px;top:988px;width:480px;list-style:none}
  .groups li{position:relative;padding-left:32px;font-size:16px;line-height:20px;font-weight:500;color:var(--grey-text);margin-bottom:11px}
  .groups li svg{position:absolute;left:0;top:2px}
  .contact-label{position:absolute;left:50px;top:1240px;padding:6px 26px;border-radius:20px;background:#ececec;border-right:4px solid var(--green);font-size:22px;font-weight:700;color:var(--dark)}
  .contact-line{position:absolute;left:50px;display:flex;align-items:center;gap:10px;font-size:22px;font-weight:600;color:var(--blue)}
  .phones{top:1300px;gap:40px}
  .phones span{display:flex;align-items:center;gap:10px}
  .email{top:1346px;font-size:18px}
  .catalyst{position:absolute;left:566px;top:925px;width:479px;height:345px;border-radius:60px;background:var(--green);border-left:6px solid var(--blue);padding:70px 40px 0 46px;color:#fff}
  .catalyst h2{font-size:17px;line-height:21px;font-weight:700;text-transform:uppercase;padding-bottom:14px;border-bottom:1.5px solid rgba(255,255,255,.8);margin-bottom:14px}
  .catalyst p{font-size:15px;line-height:19.5px;font-weight:500}
  .org{position:absolute;right:54px;top:1290px;text-align:right;color:#fff;font-weight:700;font-style:normal}
  .org-name{font-size:17px}
  .org-address{font-size:20px;margin-top:4px;white-space:nowrap}
  .org-web{font-size:18px;margin-top:10px}
</style>
</head>
<body>
<main class="flyer">
  <svg class="deco" width="1100" height="1424" viewBox="0 0 1100 1424" aria-hidden="true">
    <path d="M980 0 H1040 C1010 20 990 40 975 60 H930 C945 35 960 15 980 0Z" fill="var(--swoosh)"/>
    <path d="M1030 0 H1100 V10 C1070 20 1040 40 1020 60 H985 C1000 35 1015 15 1030 0Z" fill="var(--green)"/>
    <path d="M930 708 C1000 730 1060 760 1100 800 V820 C1050 780 990 750 900 720Z" fill="var(--green)"/>
    <path d="M880 712 C960 730 1040 770 1100 830 V850 C1030 790 950 750 860 724Z" fill="var(--swoosh)"/>
    <path d="M1100 40 H746 C640 40 556 124 556 230 V540 C556 640 630 716 740 716" fill="none" stroke="var(--green)" stroke-width="6"/>
    <path d="M0 790 H526 A37 37 0 0 1 526 864 H0Z" fill="var(--blue)"/>
    <path d="M536 786 A41 41 0 0 1 536 868" fill="none" stroke="var(--green)" stroke-width="6"/>
    <path d="M300 1424 C460 1336 640 1292 1100 1210 V1424Z" fill="var(--blue-deep)"/>
    <path d="M560 1282 C700 1268 820 1262 900 1262 L880 1270 C800 1272 690 1280 560 1290Z" fill="#999" opacity=".5"/>
  </svg>

  <svg role="img" aria-label="Night city skyline with glowing connected-technology icons" style="position:absolute;left:566px;top:46px" width="534" height="662" viewBox="0 0 534 662">
    <defs>
      <linearGradient id="sky" x1="0" y1="0" x2="0" y2="1">
        <stop offset="0" stop-color="#5b7a93"/>
        <stop offset=".55" stop-color="#2f4c66"/>
        <stop offset="1" stop-color="#17283b"/>
      </linearGradient>
    </defs>
    <path d="M534 0 H180 C80 0 0 80 0 180 V500 C0 590 70 662 170 662 H534Z" fill="url(#sky)"/>
  </svg>

  <div class="brand">
    <div class="brand-dot"></div>
    <div class="brand-name">Q-VarDT</div>
  </div>

  <h1 class="title">Copper Ridge<br>Stewardship<br>Summit</h1>
  <p class="subtitle">Making Impact Through<br>the Built Environment</p>
  <div class="rule"></div>
  <p class="presenting">Q-VarDT is presenting<br>the Copper Ridge<br>Stewardship Summit -</p>
  <p class="tagline">Making Impact Through the Built Environment.</p>

  <p class="week-band">During the first week of</p>
  <p class="date">AUGUST 2022</p>

  <p class="groups-intro"><em>One of the most exciting</em> aspects of this<br>conference will be the bringing together<br>of multiple organizations including</p>
  <ul class="groups">
    <li><svg width="16" height="16" viewBox="0 0 16 16"><circle cx="8" cy="8" r="7" fill="none" stroke="#8cb43c" stroke-width="1.6"/><path d="M4.5 8.2l2.3 2.3 4.7-5" fill="none" stroke="#8cb43c" stroke-width="1.8"/></svg>Profits and Nonprofits</li>
    <li><svg width="16" height="16" viewBox="0 0 16 16"><circle cx="8" cy="8" r="7" fill="none" stroke="#8cb43c" stroke-width="1.6"/><path d="M4.5 8.2l2.3 2.3 4.7-5" fill="none" stroke="#8cb43c" stroke-width="1.8"/></svg>K-12's and higher education</li>
    <li><svg width="16" height="16" viewBox="0 0 16 16"><circle cx="8" cy="8" r="7" fill="none" stroke="#8cb43c" stroke-width="1.6"/><path d="M4.5 8.2l2.3 2.3 4.7-5" fill="none" stroke="#8cb43c" stroke-width="1.8"/></svg>Cities and counties and other governmental agencies</li>
    <li><svg width="16" height="16" viewBox="0 0 16 16"><circle cx="8" cy="8" r="7" fill="none" stroke="#8cb43c" stroke-width="1.6"/><path d="M4.5 8.2l2.3 2.3 4.7-5" fill="none" stroke="#8cb43c" stroke-width="1.8"/></svg>Architects</li>
    <li><svg width="16" height="16" viewBox="0 0 16 16"><circle cx="8" cy="8" r="7" fill="none" stroke="#8cb43c" stroke-width="1.6"/><path d="M4.5 8.2l2.3 2.3 4.7-5" fill="none" stroke="#8cb43c" stroke-width="1.8"/></svg>Engineers</li>
    <li><svg width="16" height="16" viewBox="0 0 16 16"><circle cx="8" cy="8" r="7" fill="none" stroke="#8cb43c" stroke-width="1.6"/><path d="M4.5 8.2l2.3 2.3 4.7-5" fill="none" stroke="#8cb43c" stroke-width="1.8"/></svg>contractors to collaboratively present and discuss issues and ideas related to sustainability</li>
    <li><svg width="16" height="16" viewBox="0 0 16 16"><circle cx="8" cy="8" r="7" fill="none" stroke="#8cb43c" stroke-width="1.6"/><path d="M4.5 8.2l2.3 2.3 4.7-5" fill="none" stroke="#8cb43c" stroke-width="1.8"/></svg>Texas focus</li>
  </ul>

  <p class="contact-label">CONTACT US</p>
  <p class="contact-line phones">
    <span><svg width="22" height="22" viewBox="0 0 24 24"><path d="M6.6 10.8a15 15 0 006.6 6.6l2.2-2.2c.3-.3.7-.4 1-.2 1.1.4 2.3.6 3.6.6.6 0 1 .4 1 1V20c0 .6-.4 1-1 1A17 17 0 013 4c0-.6.4-1 1-1h3.5c.6 0 1 .4 1 1 0 1.3.2 2.5.6 3.6.1.3 0 .7-.2 1z" fill="#8cb43c"/></svg>(555) 014-2270</span>
    <span><svg width="22" height="22" viewBox="0 0 24 24"><path d="M6.6 10.8a15 15 0 006.6 6.6l2.2-2.2c.3-.3.7-.4 1-.2 1.1.4 2.3.6 3.6.6.6 0 1 .4 1 1V20c0 .6-.4 1-1 1A17 17 0 013 4c0-.6.4-1 1-1h3.5c.6 0 1 .4 1 1 0 1.3.2 2.5.6 3.6.1.3 0 .7-.2 1z" fill="#8cb43c"/></svg>(555) 018-6394</span>
  </p>
  <p class="contact-line email"><svg width="24" height="18" viewBox="0 0 24 18"><rect width="24" height="18" rx="2" fill="#8cb43c"/><path d="M1 2l11 8 11-8" fill="none" stroke="#fff" stroke-width="2"/></svg>dana.hollis@q-vardt.org</p>

  <section class="catalyst">
    <h2>This event will be a catalyst for<br>public and private project owners</h2>
    <p>to holistically gather information &amp; momentum as we bring the resources &amp; vision needed to achieve the goal of zero carbon emissions from the built environment by 2040, &amp; address water, green space and the natural environment, transportation, equity, &amp; funding, among other topics.</p>
  </section>

  <address class="org">
    <div class="org-name">Q-VarDT</div>
    <div class="org-address">418 Quarry Bend, Millbrook TX 75001</div>
    <div class="org-web">q-vardt.example.org</div>
  </address>
</main>
</body>
</html>
```